Business Cards that are elegant and wow

I want to create and print business cards that represent my brand and stand out from the rest. We want to ensure they stay in our branding and the integrity is not lost. I am happy to look at different shapes like square etc.

It will be printed on very thick cards and will be stylish .

I want to create and print business cards that represent my brand and stand out from the rest. We want to ensure they stay in ur branding and the integrity is not lost. I am happy to look at different shapes like square etc.

Target Market(s)

real estate professionals

Industry/Entity Type

Real Estate

Contact Information for Business Card

Maren Holt
hello@brightfernrealty.com.au
brightfernrealty.com.au
0487 316 252 (SMS)

Colors

Designer to choose colors to be used in the design.

Requirements
Must have
• My logo
• email
• website
• Name
Nice to have
• I like the idea of printing with foil or spot gloss. You want it to stand out in a sea.
Should not have
• I would like you to stay in my colour themes. Don't change the colour of my logo

```html
<!DOCTYPE html>
<html lang="en">
<head>
<meta charset="utf-8">
<title>Bright Fern Realty – Business Cards</title>
<link href="https://fonts.googleapis.com/css2?family=Exo+2:wght@600&family=Roboto:wght@400&display=swap" rel="stylesheet">
<style>
  :root {
    --backdrop: #2a2a2a;
    --card-dark: #1b1b1b;
    --card-light: #f1f1f1;
    --brand-blue: #1a8fd6;
    --brand-pink: #d6246b;
    --text-grey: #3d3d3d;
  }
  * { box-sizing: border-box; margin: 0; padding: 0; }
  html, body {
    width: 1200px;
    height: 672px;
    overflow: hidden;
    background: var(--backdrop);
  }
  .canvas {
    position: relative;
    width: 1200px;
    height: 672px;
  }
  .card {
    position: absolute;
    top: 178px;
    width: 300px;
    height: 300px;
    border-radius: 22px;
    display: flex;
    flex-direction: column;
    align-items: center;
    justify-content: center;
  }
  .card--front {
    left: 206px;
    background: var(--card-dark);
  }
  .card--back {
    left: 672px;
    background: var(--card-light);
  }
  .brand-name {
    font-family: "Exo 2", sans-serif;
    font-weight: 600;
    font-size: 30px;
    letter-spacing: 0.5px;
    color: var(--brand-blue);
    text-align: center;
    line-height: 1.1;
  }
  .agent-name {
    font-family: "Exo 2", sans-serif;
    font-weight: 600;
    font-size: 22px;
    color: var(--brand-blue);
    margin-top: -18px;
  }
  .contact-icons {
    display: flex;
    gap: 10px;
    margin: 16px 0 12px;
  }
  .contact-icons svg {
    width: 11px;
    height: 11px;
    fill: none;
    stroke: var(--brand-pink);
    stroke-width: 1.6;
  }
  .contact-list {
    list-style: none;
    font-family: "Roboto", sans-serif;
    font-size: 13.5px;
    line-height: 18.5px;
    color: var(--text-grey);
    text-align: center;
  }
</style>
</head>
<body>
<main class="canvas">
  <section class="card card--front" aria-label="Card front">
    <h1 class="brand-name">BRIGHT FERN<br>REALTY</h1>
  </section>

  <section class="card card--back" aria-label="Card back">
    <h2 class="agent-name">Maren Holt</h2>
    <div class="contact-icons" aria-hidden="true">
      <svg viewBox="0 0 12 12"><path d="M2 4.5 Q6 1.5 10 4.5 L9 6 L7.5 5 L7.5 4 Q6 3.5 4.5 4 L4.5 5 L3 6 Z M3.5 7 H8.5 V10.5 H3.5 Z"/></svg>
      <svg viewBox="0 0 12 12"><rect x="1" y="2.5" width="10" height="7"/><path d="M1 2.5 L6 7 L11 2.5"/></svg>
      <svg viewBox="0 0 12 12"><circle cx="6" cy="6" r="4.8"/><ellipse cx="6" cy="6" rx="2" ry="4.8"/><path d="M1.2 6 H10.8"/></svg>
    </div>
    <ul class="contact-list">
      <li>0487 316 252 (SMS)</li>
      <li>hello@brightfernrealty.com.au</li>
      <li>www.brightfernrealty.com.au</li>
    </ul>
  </section>
</main>
</body>
</html>
```